RW Soundworks Web Site Design

Need a basic site to show clients a little about what we do. We are a custom audio video company in the high-end residential market. Need a few basic but professional pages to show past projects and products we sell. No e-commerce. Should include my new logo from MarkHive.

Industry/Entity Type

Residential

Number of Pages Required

2 page

Font styles to use
Serif
Sans Serif

Colors
f78f20

Requirements
Must have
• Company Logo, Send feedback page
Nice to have
• I have no ideas about design, but I do know what I like and dislike when I see it.

```html
<!DOCTYPE html>
<html lang="en">
<head>
<meta charset="utf-8">
<title>RW Soundworks</title>
<link rel="stylesheet" href="https://fonts.googleapis.com/css2?family=Ubuntu:wght@400;500;700&family=Open+Sans:wght@400;600;700&display=swap">
<style>
:root{
  --black:#0b0b0b;
  --band:#141414;
  --footer:#222324;
  --base:#4b5655;
  --orange:#f78f20;
  --green:#8cc63f;
  --white:#ffffff;
  --muted:#bdbdbd;
  --card:rgba(18,18,18,.88);
}
*{margin:0;padding:0;box-sizing:border-box}
html,body{width:1200px;height:3371px;overflow:hidden}
body{background:var(--black);color:var(--white);font-family:"Open Sans",Arial,sans-serif;position:relative}
.photo{position:absolute;left:0;width:1200px}

/* hero */
.hero{top:0;height:506px;background:
  linear-gradient(180deg,rgba(0,0,0,0) 0%,rgba(0,0,0,0) 55%,rgba(10,9,8,.85) 100%),
  linear-gradient(90deg,#3a3128 0%,#5a4a3a 30%,#4a4038 55%,#4d6f86 72%,#6e9fbd 100%)}
.logo-tab{position:absolute;left:0;top:168px;width:445px;height:135px;background:var(--white);border-radius:0 0 60px 0;display:flex;align-items:center;justify-content:flex-end;padding-right:45px;gap:12px}
.logo-tab .mark{width:26px;height:26px;background:var(--orange)}
.logo-tab .name{font-family:"Ubuntu",sans-serif;font-weight:700;font-size:24px;color:#2a2a2a;letter-spacing:.5px}

/* nav */
.nav{position:absolute;top:506px;left:0;width:1200px;height:84px;background:var(--black);display:flex;align-items:center;padding-left:242px}
.nav .brand{font-family:"Ubuntu",sans-serif;font-weight:700;font-size:17px;letter-spacing:1px;margin-right:70px}
.nav .brand span{color:var(--orange)}
.nav ul{list-style:none;display:flex;gap:52px;font-size:13px;color:#d7d7d7}
.nav li.active{color:var(--orange);border-bottom:2px solid var(--orange);padding-bottom:4px}

/* banner */
.banner{top:590px;height:560px;background:
  radial-gradient(ellipse 520px 300px at 600px 230px,rgba(190,140,90,.55),rgba(0,0,0,0) 70%),
  linear-gradient(180deg,#2a2d33 0%,#4a3a2a 40%,#5a4230 65%,#2a1f17 100%)}
.banner h1{position:absolute;top:210px;width:100%;text-align:center;font-family:"Ubuntu",sans-serif;font-weight:700;font-size:40px;line-height:50px;text-shadow:0 2px 6px rgba(0,0,0,.7)}

.section-band{position:absolute;left:0;width:1200px;height:66px;background:var(--band);display:flex;align-items:center;justify-content:center;font-family:"Ubuntu",sans-serif;font-size:19px}

/* services */
.services{top:1216px;height:806px;background:linear-gradient(135deg,#3c2a1e 0%,#6a4428 45%,#2b1d14 100%)}
.card{position:absolute;width:327px;height:320px;background:var(--card);padding:14px 16px}
.card .thumb{height:150px;margin:-14px -16px 12px}
.card h3{font-family:"Ubuntu",sans-serif;font-size:14px;font-weight:500;margin-bottom:8px}
.card p{font-size:10.5px;line-height:15px;color:var(--muted)}
.card.c1{left:270px;top:82px}.card.c2{left:600px;top:82px}
.card.c3{left:270px;top:436px}.card.c4{left:600px;top:436px}
.c1 .thumb{background:linear-gradient(180deg,#1c2430,#3b3f48)}
.c2 .thumb{background:linear-gradient(180deg,#6d5a45,#3b3026)}
.c3 .thumb{background:linear-gradient(180deg,#d8d8d8,#8a8a8a)}
.c4 .thumb{background:linear-gradient(180deg,#1a1a1a,#5a1212 60%,#1a1a1a)}

/* contact */
.contact{position:absolute;top:2022px;left:0;width:1200px;height:523px;background:var(--black);text-align:center}
.contact h2{margin-top:108px;font-family:"Ubuntu",sans-serif;font-size:20px;font-weight:500}
.contact .sub{font-size:11px;color:var(--muted);margin-top:4px}
.form{position:absolute;left:505px;top:214px;width:185px}
.form label{display:block;font-size:10px;text-align:center;margin:6px 0 3px}
.form .field{height:16px;background:var(--white)}
.form .area{height:50px;background:var(--white)}
.form .submit{width:80px;height:18px;background:var(--white);color:#333;font-size:9px;line-height:18px;margin:10px auto 0}

/* feedback */
.feedback{top:2612px;height:438px;background:linear-gradient(180deg,#6b5a48 0%,#3a332d 50%,#2a2622 100%)}
.quote{position:absolute;left:337px;display:flex;align-items:center}
.quote .avatar{width:64px;height:64px;border-radius:50%;background:#9a8f86;border:2px solid #ddd;flex:none}
.quote .bubble{margin-left:8px;width:440px;background:rgba(60,60,60,.9);border-radius:30px;padding:9px 18px;font-size:10px;line-height:13px;color:#e6e6e6}
.quote .bubble b{color:var(--orange)}

/* footer */
.footer{position:absolute;top:3050px;left:0;width:1200px;height:169px;background:var(--footer)}
.col{position:absolute;top:22px;width:200px;font-size:10.5px;line-height:17px;color:#cfcfcf}
.col h4{color:var(--green);font-size:12px;font-weight:600;margin-bottom:4px}
.divider{position:absolute;top:20px;width:1px;height:120px;background:#555}

.base{position:absolute;top:3219px;left:0;width:1200px;height:152px;background:var(--base)}
.info{position:absolute;left:300px;display:flex;gap:12px;align-items:flex-start;font-size:10.5px;line-height:15px;color:#e8e8e8}
.copy{position:absolute;left:606px;top:40px;font-size:11px;color:var(--green)}
.social{position:absolute;left:750px;top:82px;display:flex;gap:14px}
.social span{width:26px;height:26px;border-radius:50%;background:#2f3636}
</style>
</head>
<body>

<div class="photo hero" role="img" aria-label="Photo of a luxury home theater room with a large projection screen and lounge seating"></div>
<div class="logo-tab"><span class="mark"></span><span class="name">RW Soundworks</span></div>

<nav class="nav">
  <div class="brand">RW <span>SOUNDWORKS</span></div>
  <ul>
    <li>Home</li><li>About</li><li>Services</li><li>Projects</li><li class="active">Contact Us</li><li>Blog</li>
  </ul>
</nav>

<div class="photo banner" role="img" aria-label="Photo of a sports bar with a wall of large video screens">
  <h1>Audio + Video<br>Anyplace , Anywhere , Anytime</h1>
</div>

<div class="section-band" style="top:1150px">Our Services</div>

<section class="photo services" role="img" aria-label="Photo of a private cinema with leather recliners as background">
  <article class="card c1">
    <div class="thumb" role="img" aria-label="Photo of a media room with a projection screen"></div>
    <h3>Rooms and Zones</h3>
    <p>We plan whole-home audio for every room and outdoor area. One simple keypad or app lets you choose music, set levels and group zones together, with speakers hidden neatly in walls and ceilings for a clean finish.</p>
  </article>
  <article class="card c2">
    <div class="thumb" role="img" aria-label="Photo of a home theater interior"></div>
    <h3>Home Theater Design</h3>
    <p>From a cozy media den to a full private cinema, we design seating, acoustics, projection and surround sound around your space, then calibrate every system so the picture and sound feel exactly right.</p>
  </article>
  <article class="card c3">
    <div class="thumb" role="img" aria-label="Photo of a living room with a wall mounted television"></div>
    <h3>Video Distribution</h3>
    <p>Watch any source on any screen in the house. We wire and configure distributed video so cable, streaming and media servers reach each television cleanly, with tidy racks and simple remotes for the whole family.</p>
  </article>
  <article class="card c4">
    <div class="thumb" role="img" aria-label="Photo of a touch control panel screen"></div>
    <h3>Lighting and Control Systems</h3>
    <p>Bring lighting, shades, climate and entertainment under one touch panel. Scenes for morning, movie night or away mode run with a single tap, and our team supports every system long after installation.</p>
  </article>
</section>

<section class="contact">
  <h2>Contact us today</h2>
  <p class="sub">We would love to hear about your next project</p>
  <div class="form">
    <label>Name</label><div class="field"></div>
    <label>Email</label><div class="field"></div>
    <label>Message</label><div class="area"></div>
    <div class="submit">Submit</div>
  </div>
</section>

<div class="section-band" style="top:2545px">Customer's feedback</div>

<section class="photo feedback" role="img" aria-label="Photo of a conference room with a large display as background">
  <div class="quote" style="top:50px"><div class="avatar"></div><div class="bubble"><b>Mark D.</b> The team turned our basement into a real cinema. Sound is amazing and the install was clean and on time.</div></div>
  <div class="quote" style="top:126px"><div class="avatar"></div><div class="bubble"><b>Laura P.</b> Music in every room with one app. Friendly crew, clear pricing and great follow up service.</div></div>
  <div class="quote" style="top:200px"><div class="avatar"></div><div class="bubble"><b>James K.</b> Our lighting and shades now work with one touch. We could not be happier with the result.</div></div>
  <div class="quote" style="top:270px"><div class="avatar"></div><div class="bubble"><b>Susan R.</b> Professional from design to finish. Every screen in the house works perfectly together now.</div></div>
  <div class="quote" style="top:342px"><div class="avatar"></div><div class="bubble"><b>Tom H.</b> They listened to what we wanted and delivered a system that is simple for the whole family.</div></div>
</section>

<footer class="footer">
  <div class="col" style="left:336px"><h4>Our Services</h4>Home Theater<br>Whole Home Audio<br>Lighting Control<br>Networking</div>
  <div class="divider" style="left:478px"></div>
  <div class="col" style="left:555px"><h4>Company</h4>About Us<br>Projects<br>Products We Sell</div>
  <div class="divider" style="left:725px"></div>
  <div class="col" style="left:800px"><h4>Support</h4>Contact Us<br>Send Feedback<br>Service Request</div>
</footer>

<div class="base">
  <div class="info" style="top:30px">
    <svg width="22" height="22" viewBox="0 0 24 24"><path fill="#3fb6c4" d="M6.6 10.8a15 15 0 0 0 6.6 6.6l2.2-2.2a1 1 0 0 1 1-.25 11.4 11.4 0 0 0 3.6.57 1 1 0 0 1 1 1V20a1 1 0 0 1-1 1A17 17 0 0 1 3 4a1 1 0 0 1 1-1h3.5a1 1 0 0 1 1 1c0 1.250.2 2.45.57 3.6a1 1 0 0 1-.25 1z"/></svg>
    <div>Phone: (555) 014 2290<br>info@rwsoundworks.example</div>
  </div>
  <div class="info" style="top:84px">
    <svg width="22" height="22" viewBox="0 0 24 24"><path fill="#3fb6c4" d="M12 2a7 7 0 0 0-7 7c0 5.2 7 13 7 13s7-7.8 7-13a7 7 0 0 0-7-7zm0 9.5A2.5 2.5 0 1 1 12 6.5a2.5 2.5 0 0 1 0 5z"/></svg>
    <div>120 Harbor Lane<br>Milltown, ST 00000</div>
  </div>
  <div class="copy">© 2024 RW Soundworks. All rights reserved.</div>
  <div class="social"><span></span><span></span><span></span><span></span></div>
</div>

</body>
</html>
```